Hispanic Financial Counseling and Advocate Firm seeks business card design

Looking for a clean, professional business card design. This is a firm that specializes in providing financial education, coaching, and planning to the Hispanic community. The name of the company is Valemar, which means to prosper. We need a design that is clean, professional, and invokes trust, professionalism, but also welcoming. Our logo is a plant growing from a hand to give the messaging of of being in control of growing your financial future and security. Its part of a larger organization names Celesta Financial Group, who's logo is a tree with multi colored branches. We have the back of the card designed so we just need the front designed. the back is blue, so front needs to be a different background color, not blue.

Target Market(s)

Hispanic Community looking to better their future

Industry/Entity Type

financial services

Contact Information for Business Card

contact info: Anselmo Ibarra Jr, 951-555-0147, info@celestafinancialgroup.example. Celestafinancialgroup.example. tag line: Para un futuro mas seguro!

Requirements
Must have
• basics: logo, contact info.
Nice to have
• possibly incorporate the tree logo provided somehow
Should not have
• should not look like the back, needs to be different from the back provided.

```html
<!DOCTYPE html>
<html lang="es">
<head>
<meta charset="utf-8">
<title>Valemar – Business Card</title>
<link rel="stylesheet" href="https://fonts.googleapis.com/css2?family=Montserrat:wght@400;500;700&display=swap">
<style>
  :root {
    --bg: #f1f1f1;
    --card: #ffffff;
    --green: #6ba531;
    --navy: #4b5a74;
    --white: #ffffff;
  }
  * { margin: 0; padding: 0; box-sizing: border-box; }
  html, body { width: 1200px; height: 1200px; overflow: hidden; }
  body { background: var(--bg); font-family: "Montserrat", sans-serif; position: relative; }

  .card { position: absolute; left: 281px; width: 636px; height: 364px; border-radius: 32px; overflow: hidden; }

  /* front */
  .card--front { top: 198px; background: var(--card); }
  .front-brand { position: absolute; left: 0; right: 0; top: 82px; text-align: center; }
  .brand-dot { display: block; width: 58px; height: 58px; border-radius: 50%; background: var(--green); margin: 0 auto 12px; }
  .front-brand .brand-name { font-size: 46px; font-weight: 500; color: var(--green); line-height: 1; letter-spacing: -0.5px; }
  .front-brand .brand-sub { margin-top: 8px; font-size: 12px; font-weight: 700; letter-spacing: 1.6px; color: var(--navy); }

  /* back */
  .card--back { top: 594px; background: var(--navy); }
  .back-top { position: absolute; left: 0; top: 0; width: 100%; height: 250px; background: var(--green); }
  .back-brand { position: absolute; left: 150px; top: 52px; display: flex; align-items: center; }
  .back-brand .brand-dot { width: 90px; height: 90px; margin: 0; background: var(--white); }
  .divider { margin: 0 20px 0 36px; }
  .back-brand .brand-name { font-size: 44px; font-weight: 500; color: var(--white); line-height: 1; letter-spacing: -0.5px; }
  .back-brand .brand-sub { margin-top: 8px; font-size: 12px; font-weight: 700; letter-spacing: 1.4px; color: var(--white); }
  .back-brand .tagline { font-size: 12px; font-weight: 400; color: var(--white); }

  .name-tab { position: absolute; left: 0; top: 238px; width: 303px; height: 86px; background: var(--white); border-radius: 0 43px 43px 0; display: flex; align-items: center; padding-left: 22px; }
  .person-name { font-size: 30px; font-weight: 700; color: var(--green); letter-spacing: -0.3px; white-space: nowrap; }

  .contact { position: absolute; left: 328px; top: 266px; list-style: none; }
  .contact li { display: flex; align-items: center; height: 29px; font-size: 15px; color: var(--white); }
  .contact svg { width: 14px; height: 14px; margin-right: 14px; flex: none; }
</style>
</head>
<body>

<section class="card card--front">
  <div class="front-brand">
    <span class="brand-dot"></span>
    <div class="brand-name">Valemar</div>
    <div class="brand-sub">SERVICIOS FINANCIEROS</div>
  </div>
</section>

<section class="card card--back">
  <div class="back-top"></div>
  <div class="back-brand">
    <span class="brand-dot"></span>
    <svg class="divider" width="20" height="124" viewBox="0 0 20 124"><path d="M2 2 Q22 62 2 122" fill="none" stroke="#ffffff" stroke-width="1.6"/></svg>
    <div>
      <div class="brand-name">Valemar</div>
      <div class="brand-sub">SERVICIOS FINANCIEROS</div>
      <div class="tagline">Para un futuro mas seguro</div>
    </div>
  </div>

  <div class="name-tab"><span class="person-name">Anselmo Ibarra Jr</span></div>

  <ul class="contact">
    <li>
      <svg viewBox="0 0 24 24" fill="none" stroke="#fff" stroke-width="1.6"><path d="M5 3h4l2 5-2.5 1.5a11 11 0 0 0 6 6L16 13l5 2v4a2 2 0 0 1-2 2A16 16 0 0 1 3 5a2 2 0 0 1 2-2z"/></svg>
      951-555-0147
    </li>
    <li>
      <svg viewBox="0 0 24 24" fill="none" stroke="#fff" stroke-width="1.6"><rect x="2" y="5" width="20" height="14" rx="1"/><path d="M2 6l10 7 10-7"/></svg>
      Celestafinancialgroup.example
    </li>
    <li>
      <svg viewBox="0 0 24 24" fill="none" stroke="#fff" stroke-width="1.6"><circle cx="12" cy="12" r="10"/><path d="M2 12h20M12 2c3 3 3 17 0 20M12 2c-3 3-3 17 0 20"/></svg>
      info@celestafinancialgroup.example
    </li>
  </ul>
</section>

</body>
</html>
```